Italian restaurant needs new site

Need to make our website better.

Must have reservation module

Must be able to sell wine tasting tours and wine pairing tours and intégrate with lumo desk

Blog

Social media

Wandermeter ranking and last review.

Number of Pages Required

1 page

Font styles to use
Serif

Requirements
Must have
• Reservation module
• Marketplace to buy wine pairings and gift certificates
• Wandermeter review
• Chatterbay posts
• All info from old site

```html
<!DOCTYPE html>
<html lang="en">
<head>
<meta charset="utf-8">
<title>Rosso Tavola — Italian Cuisine &amp; Wine Bar</title>
<link href="https://fonts.googleapis.com/css2?family=Cinzel:wght@400;700&family=Open+Sans:wght@400;600;700&display=swap" rel="stylesheet">
<style>
:root{
  --red:#a3121a;
  --red-deep:#7d0d12;
  --orange:#e0521d;
  --ink:#2b2b2b;
  --muted:#777;
  --line:#e4e4e4;
  --paper:#ffffff;
  --soft:#f4f4f4;
  --night:#141212;
  --blue:#3f5e9c;
}
*{box-sizing:border-box;margin:0;padding:0}
html,body{width:1200px;height:2900px;overflow:hidden}
body{font-family:"Open Sans",Arial,sans-serif;color:var(--ink);background:var(--paper);font-size:12px;line-height:1.6}
.serif{font-family:"Cinzel",Georgia,serif}
section,header,footer{position:relative;width:1200px;overflow:hidden}
.btn{display:inline-block;background:var(--orange);color:#fff;font-size:10px;font-weight:700;letter-spacing:.08em;text-transform:uppercase;padding:9px 22px;border-radius:20px}
.section-title{font-family:"Cinzel",Georgia,serif;color:var(--red);font-size:26px;font-weight:700;text-align:center;letter-spacing:.04em}
.section-intro{width:520px;margin:8px auto 0;text-align:center;color:var(--muted);font-size:11px;line-height:1.5}

/* hero */
.hero{height:500px;background:var(--night)}
.hero-photo{position:absolute;inset:0;background:radial-gradient(ellipse at 72% 55%,#6b1d12 0%,#3a120e 35%,#120d0c 75%)}
.nav{position:absolute;top:0;left:0;width:1200px;height:48px;background:rgba(0,0,0,.45);display:flex;justify-content:center;align-items:center;gap:56px}
.nav a{color:#eee;font-size:11px;font-weight:600;letter-spacing:.1em;text-transform:uppercase;text-decoration:none}
.brand-tab{width:130px;height:92px;background:var(--paper);display:flex;align-items:center;justify-content:center;margin-top:44px;box-shadow:0 3px 10px rgba(0,0,0,.4)}
.brand{font-family:"Cinzel",Georgia,serif;font-weight:700;color:var(--red);font-size:17px;line-height:1.1;text-align:center}
.hero-copy{position:absolute;left:60px;top:250px;color:#fff}
.hero-copy h1{font-family:"Cinzel",Georgia,serif;font-size:44px;font-weight:700;line-height:1.12;letter-spacing:.03em}
.hero-copy p{font-size:13px;margin-top:8px;color:#ddd}

/* about */
.about{height:320px;background:var(--paper)}
.about-copy{position:absolute;left:160px;top:55px;width:520px}
.about-copy h2{font-family:"Cinzel",Georgia,serif;color:var(--red);font-size:20px;font-weight:700;line-height:1.25}
.about-copy p{font-size:11px;color:var(--muted);margin:14px 0 20px;line-height:1.7}
.about-photo{position:absolute;left:760px;top:20px;width:260px;height:300px;background:linear-gradient(180deg,#e9e6e2,#bcb7b2 60%,#2a2a2a)}

/* wine */
.wines{height:380px;background:var(--paper);padding-top:34px;border-top:1px solid var(--line)}
.side-food{position:absolute;left:0;top:40px;width:80px;height:280px;background:linear-gradient(180deg,#c98a45,#8a3b1f 55%,#5e7a2e)}
.wine-grid{position:absolute;left:240px;top:120px;width:720px;display:flex;gap:38px}
.wine-card{width:151px;text-align:center}
.wine-img{height:150px;background:linear-gradient(160deg,#3a2a1d,#7b6247)}
.wine-card:nth-child(2) .wine-img{background:linear-gradient(160deg,#4f6e2a,#a7b65c)}
.wine-card:nth-child(3) .wine-img{background:linear-gradient(160deg,#4a0f14,#b64a3e)}
.wine-card:nth-child(4) .wine-img{background:linear-gradient(160deg,#2c2420,#a58c6a)}
.wine-card h3{font-family:"Cinzel",Georgia,serif;font-size:13px;margin-top:12px}
.wine-card .origin{font-size:10px;color:var(--muted)}
.wine-card .price{color:var(--red);font-weight:700;font-size:11px}

/* reservation */
.reserve{height:400px;background:var(--night)}
.reserve-photo{position:absolute;inset:0;background:linear-gradient(180deg,#1d1a18,#3b342f 50%,#1a1716)}
.reserve-copy{position:absolute;top:70px;left:0;width:1200px;text-align:center;color:#fff}
.reserve-copy h2{font-family:"Cinzel",Georgia,serif;font-size:40px;line-height:1.1;letter-spacing:.04em}
.reserve-copy h2 span{display:block;color:#e04a2b}
.reserve-copy p{width:560px;margin:14px auto 0;font-size:11px;color:#ccc;line-height:1.5}
.widget{width:70px;height:44px;margin:22px auto 24px;border:2px solid #ddd;border-radius:3px;display:flex;align-items:center;justify-content:center;font-size:9px;font-weight:700;color:#fff}

/* blog */
.blog{height:450px;background:var(--paper);padding-top:24px;border-top:1px solid var(--line)}
.blog-grid{position:absolute;left:240px;top:130px;width:720px;display:flex;gap:18px}
.post{width:228px;background:var(--paper);box-shadow:0 1px 5px rgba(0,0,0,.18)}
.post-img{position:relative;height:130px;background:linear-gradient(150deg,#a33b24,#e3a54d)}
.post:nth-child(2) .post-img{background:linear-gradient(150deg,#3d2a1d,#c47a35)}
.post:nth-child(3) .post-img{background:linear-gradient(150deg,#2b2440,#c0425a)}
.date{position:absolute;left:8px;top:8px;width:34px;height:38px;background:var(--red);color:#fff;text-align:center;font-size:9px;line-height:1.1;padding-top:5px}
.date b{display:block;font-size:14px}
.post h3{font-size:11px;font-weight:700;padding:12px 12px 6px}
.post p{font-size:10px;color:var(--muted);padding:0 12px;line-height:1.5}
.post .meta{display:flex;justify-content:space-between;font-size:9px;color:var(--muted);border-top:1px solid var(--line);margin-top:10px;padding:7px 12px}

/* social */
.social{height:350px;background:var(--paper)}
.panel{position:absolute;top:20px;width:320px;height:310px;border:1px solid var(--line)}
.panel.feed{left:240px}
.panel.reviews{left:640px}
.panel-head{height:34px;color:#fff;font-family:"Cinzel",Georgia,serif;font-size:13px;font-weight:700;padding:8px 12px;display:flex;justify-content:space-between;align-items:center}
.feed .panel-head{background:var(--blue)}
.reviews .panel-head{background:var(--red-deep)}
.panel-head small{font-family:"Open Sans",Arial,sans-serif;font-size:9px;font-weight:600;background:rgba(255,255,255,.2);padding:2px 8px}
.item{display:flex;gap:10px;padding:10px 12px;border-bottom:1px solid var(--line)}
.thumb{flex:none;width:48px;height:40px;background:linear-gradient(150deg,#b7652d,#6c2a18)}
.item h4{font-size:10px;font-weight:700;color:var(--ink)}
.feed .item h4{color:var(--orange)}
.item p{font-size:9px;color:var(--muted);line-height:1.4}
.panel-foot{font-size:9px;color:var(--muted);padding:8px 12px}

/* contact */
.contact{height:290px;background:var(--red-deep)}
.contact-copy{position:absolute;left:240px;top:34px;color:#fff;width:320px}
.contact-copy h2{font-family:"Cinzel",Georgia,serif;font-size:22px;font-weight:400;margin-bottom:16px}
.contact-row{display:flex;gap:10px;align-items:center;font-size:10px;margin-bottom:8px;color:#f1dcdc}
.contact-row svg{flex:none}
.socials{display:flex;gap:6px;margin:12px 0 18px}
.socials span{width:16px;height:16px;border-radius:50%;background:#fff;opacity:.85}
.map{position:absolute;left:600px;top:0;width:600px;height:290px;background:linear-gradient(135deg,#e9e6df,#d9e4ea 55%,#a8c6dc)}

/* footer */
.site-footer{height:210px;background:var(--paper)}
.foot-brand{position:absolute;left:240px;top:30px;width:150px}
.foot-brand .brand{font-size:18px;text-align:left}
.foot-brand p{font-size:9px;color:var(--muted);margin-top:10px;line-height:1.5}
.foot-col{position:absolute;top:30px}
.foot-col h4{font-size:10px;font-weight:700;text-transform:uppercase;letter-spacing:.06em;margin-bottom:8px}
.foot-col ul{list-style:none;font-size:9px;color:var(--muted);line-height:2}
.copyright{position:absolute;left:0;bottom:14px;width:1200px;text-align:center;font-size:9px;color:var(--muted);border-top:1px solid var(--line);padding-top:10px}
</style>
</head>
<body>

<header class="hero">
  <div class="hero-photo" role="img" aria-label="Candlelit table with wine bottles, glasses and fruit"></div>
  <nav class="nav">
    <a href="#">Home</a>
    <a href="#">Reservation</a>
    <div class="brand-tab"><span class="brand">Rosso<br>Tavola</span></div>
    <a href="#">Menu</a>
    <a href="#">Contact</a>
  </nav>
  <div class="hero-copy">
    <h1>The Best Italian<br>Cusine &amp; Wine Bar</h1>
    <p>Rosso Tavola Italian restaurant in Cabo San Lucas</p>
  </div>
</header>

<section class="about">
  <div class="about-copy">
    <h2>Rosso Tavola Italian Restaurant<br>in Cabo San Lucas</h2>
    <p>Rosso Tavola brings the warmth of a true Italian kitchen to the heart of Cabo San Lucas. Our chefs prepare handmade pasta, wood fired dishes and seasonal plates using fresh local produce and fine imported ingredients. Pair every course with a glass from our cellar, chosen by our sommelier to match the flavours of the menu. Join us for a relaxed dinner, a private celebration or a guided wine tasting evening, and let our team make every visit one to remember with friends and family.</p>
    <span class="btn">Reservation Now</span>
  </div>
  <div class="about-photo" role="img" aria-label="Waiter in a dark suit holding a tray with a wine bottle"></div>
</section>

<section class="wines">
  <div class="side-food" role="img" aria-label="Plate of bread, cured meats and fresh vegetables"></div>
  <h2 class="section-title">Latest Wine</h2>
  <p class="section-intro">Discover the bottles our sommelier loves this season, from crisp sparkling wines to rich reds, each one ready for a tasting or to pair with your dinner.</p>
  <div class="wine-grid">
    <div class="wine-card"><div class="wine-img" role="img" aria-label="Sparkling wine bottle and glasses"></div><h3>Sparkling Wine</h3><div class="origin">Lambrusco Emilia</div><div class="price">$120</div></div>
    <div class="wine-card"><div class="wine-img" role="img" aria-label="White wine in a vineyard"></div><h3>White Wine</h3><div class="origin">Pinot Grigio Veneto</div><div class="price">$95</div></div>
    <div class="wine-card"><div class="wine-img" role="img" aria-label="Red wine glasses on a table"></div><h3>Red Wine</h3><div class="origin">Chianti Classico</div><div class="price">$110</div></div>
    <div class="wine-card"><div class="wine-img" role="img" aria-label="House wine carafe and bottles"></div><h3>House Wine</h3><div class="origin">Rosso di Casa</div><div class="price">$60</div></div>
  </div>
</section>

<section class="reserve">
  <div class="reserve-photo" role="img" aria-label="Dim restaurant dining room with set tables"></div>
  <div class="reserve-copy">
    <h2>Mak Your Reservation<span>Online Now</span></h2>
    <p>Book a table in a few clicks and choose your time, party size and any special request. You can also reserve wine tasting tours and wine pairing dinners with our online booking partner.</p>
    <div class="widget">lumo desk</div>
    <span class="btn">Book a Table</span>
  </div>
</section>

<section class="blog">
  <h2 class="section-title">Our Blog</h2>
  <p class="section-intro">Stories from our kitchen and cellar, new dishes on the menu, upcoming wine evenings and tips from our chefs on enjoying Italian food at home.</p>
  <div class="blog-grid">
    <article class="post"><div class="post-img" role="img" aria-label="Italian dishes served on a table"><div class="date"><b>15</b>Jun</div></div><h3>It is a long established fact</h3><p>Our chef shares the secret behind the fresh pasta served every night.</p><div class="meta"><span>By Admin</span><span>3 Comments</span></div></article>
    <article class="post"><div class="post-img" role="img" aria-label="Wine glasses and appetisers"><div class="date"><b>22</b>Jun</div></div><h3>It is a long established fact</h3><p>A guide to pairing regional wines with classic antipasti plates.</p><div class="meta"><span>By Admin</span><span>5 Comments</span></div></article>
    <article class="post"><div class="post-img" role="img" aria-label="Evening bar with colourful lights"><div class="date"><b>30</b>Jun</div></div><h3>It is a long established fact</h3><p>Join our summer tasting nights with live music on the terrace.</p><div class="meta"><span>By Admin</span><span>2 Comments</span></div></article>
  </div>
</section>

<section class="social">
  <div class="panel feed">
    <div class="panel-head">Chatterbay Feed <small>Follow</small></div>
    <div class="item"><div class="thumb" role="img" aria-label="Pizza fresh from the oven"></div><div><h4>Rosso Tavola</h4><p>Fresh pizza out of the wood oven tonight, come and taste it.</p></div></div>
    <div class="item"><div class="thumb" role="img" aria-label="Pasta dish"></div><div><h4>Rosso Tavola</h4><p>New seasonal pasta on the menu this week with local herbs.</p></div></div>
    <div class="item"><div class="thumb" role="img" aria-label="Dessert plate"></div><div><h4>Rosso Tavola</h4><p>Our tiramisu is back by popular demand, made every morning.</p></div></div>
    <div class="item"><div class="thumb" role="img" aria-label="Wine tasting table"></div><div><h4>Rosso Tavola</h4><p>Wine tasting tour seats are open for Friday, book online.</p></div></div>
  </div>
  <div class="panel reviews">
    <div class="panel-head">Wandermeter Reviews</div>
    <div class="item"><div class="thumb" role="img" aria-label="Dining room"></div><div><h4>Lovely dinner and great wine</h4><p>Friendly staff, perfect pasta and a wonderful view.</p></div></div>
    <div class="item"><div class="thumb" role="img" aria-label="Plated main course"></div><div><h4>Best Italian food in town</h4><p>The wine pairing was a highlight of our whole trip.</p></div></div>
    <div class="item"><div class="thumb" role="img" aria-label="Table for two"></div><div><h4>Perfect anniversary evening</h4><p>Warm service and a menu full of real Italian flavour.</p></div></div>
    <div class="item"><div class="thumb" role="img" aria-label="Wine cellar"></div><div><h4>A must for wine lovers</h4><p>Great tasting tour, we will be back next year.</p></div></div>
    <div class="panel-foot">Ranked #4 of 380 restaurants in Cabo San Lucas</div>
  </div>
</section>

<section class="contact">
  <div class="contact-copy">
    <h2>Contact Us</h2>
    <div class="contact-row"><svg width="12" height="14" viewBox="0 0 12 14"><path d="M6 0a5 5 0 0 1 5 5c0 4-5 9-5 9S1 9 1 5a5 5 0 0 1 5-5z" fill="#fff"/><circle cx="6" cy="5" r="2" fill="#7d0d12"/></svg>Calle Marina 27, Centro, Cabo San Lucas</div>
    <div class="contact-row"><svg width="12" height="12" viewBox="0 0 12 12"><path d="M2 1l2 0 1 3-1.5 1a7 7 0 0 0 3.5 3.5L8 7l3 1v2c0 1-1 1-1 1A10 10 0 0 1 1 2c0 0 0-1 1-1z" fill="#fff"/></svg>+52 600 555 0148</div>
    <div class="contact-row"><svg width="12" height="10" viewBox="0 0 12 10"><rect x="0.5" y="0.5" width="11" height="9" fill="none" stroke="#fff"/><path d="M.5.5 6 5l5.5-4.5" fill="none" stroke="#fff"/></svg>hello@rossotavola.example</div>
    <div class="socials"><span></span><span></span><span></span><span></span></div>
    <span class="btn">Send a Message</span>
  </div>
  <div class="map" role="img" aria-label="Street map of Cabo San Lucas marina and coastline with restaurant location"></div>
</section>

<footer class="site-footer">
  <div class="foot-brand"><span class="brand">Rosso Tavola</span><p>Italian cuisine and wine bar serving handmade dishes in Cabo San Lucas.</p></div>
  <div class="foot-col" style="left:440px"><h4>Quick Links</h4><ul><li>Home</li><li>About</li><li>Blog</li><li>Contact</li></ul></div>
  <div class="foot-col" style="left:600px"><h4>Menu</h4><ul><li>Starters</li><li>Pasta</li><li>Wine List</li><li>Gift Cards</li></ul></div>
  <div class="foot-col" style="left:800px"><h4>Contact Us</h4><ul><li>Calle Marina 27, Cabo San Lucas</li><li>+52 600 555 0148</li><li>hello@rossotavola.example</li></ul></div>
  <div class="copyright">Copyright © 2024 Rosso Tavola. All Rights Reserved.</div>
</footer>

</body>
</html>
```